Financial Advisor needs waiting room sign

I am a financial advisor that works with a number of accountants to develop prospects. I am looking for a 18"x24" sign to hang in their office waiting rooms to help develop prospect interest in my services. My original idea was to list all of our services in a jumbled way on the sign and on the bottom have something like "Confused? We have the answers?" "Questions - We have answers" Our logo on the bottom. While I think this is still a good idea when I try to design it - it does not work. I am open to other ideas. Here is a list of our services (list in no particular order) and I will attach our logo. List: Plovance, Plovance Supplement, Plovance Advantage, Truvely, Part A, Part B, Part D, Social Security, Turning 65, Annuities, Fixed Index Annuities, Rollovers, 401k, 403b, Investments, Stock Market, Mutual Funds, Term Insurance, Life Insurance, Final Expense, Long Term Care, Mortgage Protection, 403B / 457 Not for Profit Set Up, 403B / TSA Plans, Annuities, Asset Protection, Charitable Giving, College Funding, Estate Planning, Fixed Indexed Annuities, Guaranteed Income, IRA & 401(K) Assets and Planning, IRA, 401(K), 403(B) Rollovers, Lifetime Income Planning, Retirement Income Planning, Safe Money Options, Social Security, Tactical Asset Allocation

```html
<!DOCTYPE html>
<html lang="en">
<head>
<meta charset="utf-8">
<title>Harlowe Ridge Capital – Waiting Room Sign</title>
<link rel="stylesheet" href="https://fonts.googleapis.com/css2?family=Crimson+Text&family=Fira+Sans:ital,wght@1,800&display=swap">
<style>
  :root {
    --paper: #ffffff;
    --brand-green: #4f7a1e;
    --field-top: #74aa47;
    --field-bottom: #4e7336;
    --bar: #4c7235;
    --text-light: #ffffff;
  }
  html, body {
    margin: 0;
    padding: 0;
    width: 926px;
    height: 1200px;
    overflow: hidden;
    background: var(--paper);
  }
  .sign {
    position: relative;
    width: 926px;
    height: 1200px;
    overflow: hidden;
    background: var(--paper);
  }
  .brand-bar {
    position: absolute;
    left: 0;
    top: 0;
    width: 926px;
    height: 278px;
    background: var(--paper);
  }
  .brand {
    position: absolute;
    left: 158px;
    top: 100px;
    display: flex;
    align-items: center;
    gap: 22px;
  }
  .brand-dot {
    width: 78px;
    height: 78px;
    border-radius: 50%;
    background: var(--brand-green);
  }
  .brand-name {
    font-family: "Crimson Text", serif;
    font-size: 46px;
    color: var(--brand-green);
    letter-spacing: 1px;
    white-space: nowrap;
  }
  .field {
    position: absolute;
    left: 0;
    top: 278px;
    width: 926px;
    height: 922px;
    background: linear-gradient(to bottom, var(--field-top) 0%, var(--field-bottom) 72%, var(--field-bottom) 100%);
  }
  .growth-bars {
    position: absolute;
    left: 0;
    top: 0;
  }
  .headline {
    position: absolute;
    left: 80px;
    top: 84px;
    margin: 0;
    font-family: "Fira Sans", sans-serif;
    font-style: italic;
    font-weight: 800;
    font-size: 46px;
    line-height: 63px;
    letter-spacing: -1px;
    color: var(--text-light);
  }
  .services {
    position: absolute;
    left: 120px;
    top: 470px;
    width: 686px;
    margin: 0;
    font-family: "Crimson Text", serif;
    font-size: 25px;
    line-height: 33.4px;
    color: var(--text-light);
    text-align: justify;
    hyphens: auto;
  }
</style>
</head>
<body>
<main class="sign">
  <header class="brand-bar">
    <div class="brand">
      <span class="brand-dot" aria-hidden="true"></span>
      <span class="brand-name">Harlowe Ridge Capital</span>
    </div>
  </header>

  <section class="field">
    <svg class="growth-bars" width="926" height="922" viewBox="0 0 926 922" aria-hidden="true">
      <rect x="79" y="404" width="243" height="518" fill="var(--bar)"/>
      <rect x="342" y="332" width="242" height="590" fill="var(--bar)"/>
      <rect x="604" y="254" width="243" height="668" fill="var(--bar)"/>
    </svg>

    <h1 class="headline">Questions?<br>We have the answers!</h1>

    <p class="services" lang="en">Plovance | Plovance Supplement | Plovance Advantage | Truvely | Part A | Part B | Part D | Social Security | Turning 65 | Annuities | Fixed Index Annuities | Rollovers | 401k | 403b | Investments | Stock Market | Mutual Funds | Term Insurance | Life Insurance | Final Expense | Long Term Care | Mortgage Protection | 403B / 457 Not for Profit Set Up | 403B / TSA Plans | Annuities | Asset Protection | Charitable Giving | College Funding | Estate Planning | Fixed Indexed Annuities | Guaranteed Income | IRA &amp; 401(K) Assets and Planning | IRA | 401(K) | 403(B) Rollovers | Life&shy;time Income Planning | Retirement Income Planning | Safe Money Options | Social Security | Tactical Asset Allocation</p>
  </section>
</main>
</body>
</html>
```